Lantern Tax needs a postcard for Tax Resolutions Services

Lantern Tax specializes in helping taxpayers solve their problems with the QTB or state tax agencies. Whether it's back taxes, errors by other tax preparers or non paid employer taxes. We handle everything including but not limited to tax return amendments, penalty abatements, installment agreements, Injured/Innocent Spouse, Audits, Offers In Compromise, Tax Liens, and Tax Levys.

Primarily this postcard will be sent to taxpayers who have had a tax lien filed against them recently (in the past 30-90 days). We don't do hard sales, but want to urge prospects that there are ways to either lower their tax debt or get into manageable payments so that it's not so over whelming for them. Our ultimate goal is to help the taxpayers navigate this process and make it as painless for them as possible.

Target Market(s)

Typically small businesses owners and self-employed independent contractors ages 35-55 (who owe back taxes)

Industry/Entity Type

Accountant

Font styles to use
Serif
Sans Serif

Colors

Designer to choose colors to be used in the design.

Requirements
Must have
• Company logo, call to action with phone number,
• Please submit in flat format, with one side on top of the other. So that both sides can be easily seen and red. 3D views not necessary.
• Use colors from logo - Gold #C6A734, Purple: 5F1547
Nice to have
• Notification that prospects can schedule consultations online
Should not have
• No cartoony feel.
• Photos from my website

```html
<!DOCTYPE html>
<html lang="en">
<head>
<meta charset="utf-8">
<title>Lantern Tax Postcard</title>
<link href="https://fonts.googleapis.com/css2?family=Cabin:wght@400;500;600&family=Lato:wght@400;700&display=swap" rel="stylesheet">
<style>
:root{
  --gold:#bf9a30;
  --gold-light:#c9a940;
  --ink:#2b2b2b;
  --muted:#555;
  --panel:#eff1f2;
  --line:#b9b9b9;
  --bg:#e7e7e5;
  --white:#fff;
}
*{box-sizing:border-box;margin:0;padding:0}
html,body{width:924px;height:1200px;overflow:hidden;background:var(--bg)}
body{position:relative;font-family:'Lato',sans-serif;color:var(--ink)}
.card{position:absolute;left:97px;width:711px;height:458px;background:var(--white);box-shadow:0 2px 8px rgba(0,0,0,.18);overflow:hidden}
.card-front{top:83px}
.card-back{top:639px}

/* front */
.hero{position:absolute;left:0;top:0;width:711px;height:341px;background:linear-gradient(160deg,#b7b1a4 0%,#d6cdb6 40%,#a79d8a 75%,#8f8a82 100%)}
.hero-rule{position:absolute;left:0;top:341px;width:711px;height:4px;background:linear-gradient(90deg,var(--gold) 0%,var(--gold-light) 70%,rgba(201,169,64,0) 100%)}
.headline{position:absolute;left:26px;font-family:'Cabin',sans-serif;font-weight:500;font-size:36px;line-height:1;display:flex;align-items:center;padding-left:14px}
.headline-top{top:36px;width:369px;height:66px;background:rgba(245,245,245,.92);color:var(--gold)}
.headline-bottom{top:111px;width:270px;height:59px;background:var(--gold);color:var(--white)}
.brand{position:absolute;display:flex;align-items:center;gap:7px;font-family:'Cabin',sans-serif;font-weight:600;color:var(--gold);font-size:21px;line-height:1}
.brand-mark{width:14px;height:14px;background:var(--gold)}
.card-front .brand{left:26px;top:395px}
.pitch{position:absolute;left:257px;top:363px;width:426px}
.pitch h2{font-family:'Cabin',sans-serif;font-weight:500;font-size:16px;color:var(--gold);margin-bottom:3px}
.pitch p{font-size:10.3px;line-height:1.27;text-align:justify;color:var(--ink)}
.pitch p + p{margin-top:4px;text-align:left}
.accent{color:var(--gold)}

/* back */
.services-title{position:absolute;left:28px;top:26px;font-family:'Cabin',sans-serif;font-weight:500;font-size:17px;line-height:1.3;color:var(--gold)}
.services{position:absolute;top:80px;list-style:none;font-size:11.5px;color:var(--muted)}
.services li{display:flex;align-items:center;gap:5px;height:17.6px}
.services svg{width:8px;height:8px;flex:none}
.services-left{left:33px}
.services-right{left:195px}
.reassure{position:absolute;left:28px;top:157px;width:320px;font-size:11.2px;line-height:1.27;color:var(--muted)}
.memberships{position:absolute;left:18px;top:206px;width:330px;height:66px;background:var(--panel);display:flex;align-items:center;gap:26px;padding-left:18px}
.badge{height:36px;background:#d7dadd;border-radius:3px}
.badge-a{width:130px}
.badge-b{width:148px}
.contact{position:absolute;left:18px;top:303px;width:330px;height:129px;background:var(--gold)}
.portrait{position:absolute;left:31px;top:286px;width:114px;height:138px;border:2px solid var(--white);background:linear-gradient(180deg,#2a2624 0%,#3d3431 55%,#1c1b1b 100%)}
.contact-name{position:absolute;left:161px;top:316px;font-family:'Cabin',sans-serif;font-size:21px;color:var(--white)}
.contact-list{position:absolute;left:162px;top:352px;list-style:none;font-size:10.3px;color:var(--white);line-height:1.35}
.contact-list li{display:flex;gap:6px;margin-bottom:4px}
.contact-list svg{width:8px;height:8px;flex:none;margin-top:3px}
.stamp{position:absolute;left:605px;top:24px;width:75px;height:72px;border:1px solid #aaa}
.address-line{position:absolute;left:449px;width:233px;height:1px;background:var(--line)}
.card-back .brand{left:475px;top:355px}
.site-note{position:absolute;left:430px;top:396px;width:300px;text-align:center;font-size:11.3px;color:var(--muted)}
.site-url{position:absolute;left:430px;top:413px;width:300px;text-align:center;font-size:14.5px;letter-spacing:.3px;color:var(--ink)}
</style>
</head>
<body>

<section class="card card-front">
  <div class="hero" role="img" aria-label="Photo of a stressed man with his head in his hands at a desk with a laptop, calculator and glasses"></div>
  <div class="hero-rule"></div>
  <div class="headline headline-top">Financial Freedom</div>
  <div class="headline headline-bottom">From The QTB</div>

  <div class="brand"><span class="brand-mark"></span>LANTERN TAX</div>

  <div class="pitch">
    <h2>Are you having problems with the QTB?</h2>
    <p>Lantern Tax in Millbrook is here to help you resolve your tax problems and put an end to the misery that the QTB can put you through. We pride ourselves on being very efficient, affordable, and, of course, extremely discrete.</p>
    <p>Please call our office at <span class="accent">(555) 014-2290</span> to set up a free consultation.</p>
  </div>
</section>

<section class="card card-back">
  <h2 class="services-title">We can help you with the following<br>QTB tax problems:</h2>

  <svg width="0" height="0" style="position:absolute">
    <defs>
      <symbol id="tick" viewBox="0 0 10 10"><rect x="0.7" y="0.7" width="8.6" height="8.6" fill="none" stroke="#bf9a30" stroke-width="1.2"/><path d="M2.5 5l2 2 3.5-4" fill="none" stroke="#bf9a30" stroke-width="1.3"/></symbol>
    </defs>
  </svg>

  <ul class="services services-left">
    <li><svg><use href="#tick"/></svg>Wage Garnishment</li>
    <li><svg><use href="#tick"/></svg>Bank Levy</li>
    <li><svg><use href="#tick"/></svg>Threatening Letters</li>
    <li><svg><use href="#tick"/></svg>QTB Audit Notification</li>
  </ul>
  <ul class="services services-right">
    <li><svg><use href="#tick"/></svg>Non-Filing</li>
    <li><svg><use href="#tick"/></svg>Liens</li>
    <li><svg><use href="#tick"/></svg>Offers-in-Compromise</li>
    <li><svg><use href="#tick"/></svg>Innocent Spouse</li>
  </ul>

  <p class="reassure">Resolve your QTB tax problem with the peace of mind that you are in good hands, <span class="accent">please call us at (555) 014-2290</span> or contact us to set up a free consultation.</p>

  <div class="memberships">
    <div class="badge badge-a" role="img" aria-label="Professional association membership badge"></div>
    <div class="badge badge-b" role="img" aria-label="Enrolled agents association membership badge"></div>
  </div>

  <div class="contact"></div>
  <div class="portrait" role="img" aria-label="Portrait photo of the enrolled agent"></div>
  <div class="contact-name">Dana Ellery EA</div>
  <ul class="contact-list">
    <li><svg viewBox="0 0 10 10"><rect width="10" height="10" fill="#fff"/><path d="M5 2a2 2 0 0 1 2 2c0 1.5-2 4-2 4S3 5.5 3 4a2 2 0 0 1 2-2z" fill="#bf9a30"/></svg><span>1840 Harbor Mill Rd, Suite 120<br>Millbrook, GA 30000</span></li>
    <li><svg viewBox="0 0 10 10"><rect width="10" height="10" fill="#fff"/><path d="M3 2.2l1.2 1.6-.7.8c.4.9 1 1.5 1.9 1.9l.8-.7 1.6 1.2-.8 1C4.8 7.6 2.4 5.2 2 3z" fill="#bf9a30"/></svg><span>(555) 014-4TAX</span></li>
    <li><svg viewBox="0 0 10 10"><rect width="10" height="10" fill="#fff"/><rect x="2" y="3" width="6" height="4" fill="none" stroke="#bf9a30" stroke-width=".9"/><path d="M2 3l3 2.2L8 3" fill="none" stroke="#bf9a30" stroke-width=".9"/></svg><span>dana.ellery@lanterntax.com</span></li>
  </ul>

  <div class="stamp"></div>
  <div class="address-line" style="top:179px"></div>
  <div class="address-line" style="top:212px"></div>
  <div class="address-line" style="top:245px"></div>
  <div class="address-line" style="top:278px"></div>

  <div class="brand"><span class="brand-mark"></span>LANTERN TAX</div>
  <p class="site-note">For more information please visit our website</p>
  <p class="site-url">www.lanterntax.com</p>
</section>

</body>
</html>
```